Etiketten für Wein und Sekt
Zielgruppe
Sekt- und Weinherstellung
Zielgruppe 25 - 60 Jahre
Aufgabenstellung
Wir führen ein neues Produkt in den Markt ein:
gewünschter Name: The Velvet Dusk Mood
Hervorgehoben werden soll 'Velvet Dusk'
auf dieser Basis suchern wir einmal das Etikett für den WEIN
und einmal das Etikett für den SEKT (gleiches Design/Designfamilie)
Beim Sekt dachten wir an den Zusatz Sparkling auf dem Etikett?
Achtung, es handelt sich hier um keinen Eiswein !
Damit darf unser Produkt nicht in Verbindung gebracht werden (dt. Weinrecht)
Unser Wein/Sekt ist ein fruchtiger Rose Wein/Sekt
Ein Cuvée aus regionalen Rebsorten
Beim Trinkgenuss sollen die Gedanken an gefrorene Beeren/Trauben gehen.
Wir dachten an Beerentöne und Rosegold (wie der Inhalt)
Aktuell verwenden wir Etikettenformen in Rechteckgröße horizontal oder vertikal
Besten Dank im Voraus !!

```html
<!DOCTYPE html>
<html lang="en">
<head>
<meta charset="utf-8">
<title>The Velvet Dusk Mood – Sparkling Wine Label</title>
<link rel="stylesheet" href="https://fonts.googleapis.com/css2?family=Playfair+Display:wght@600&family=Archivo:wght@800&family=Allison&display=swap">
<style>
  :root {
    --berry-deep: #7a0c46;
    --berry-dark: #5c1a3a;
    --berry-mid: #9a4c70;
    --berry-light: #b9698d;
    --frost: #e6d2db;
    --white: #ffffff;
  }
  * { margin: 0; padding: 0; box-sizing: border-box; }
  html, body {
    width: 1200px;
    height: 900px;
    overflow: hidden;
    background: var(--berry-light);
  }
  .label {
    position: relative;
    width: 1200px;
    height: 900px;
    overflow: hidden;
    background: radial-gradient(ellipse 62% 60% at 50% 50%,
      var(--berry-light) 0%, var(--berry-mid) 55%, var(--berry-dark) 82%, #4a1230 100%);
  }
  .frost-frame {
    position: absolute;
    inset: 0;
    background: radial-gradient(ellipse 75% 78% at 50% 50%,
      rgba(230,210,219,0) 58%, rgba(230,210,219,0.35) 78%, rgba(236,222,228,0.85) 100%);
  }
  .brand {
    position: absolute;
    left: 0;
    right: 0;
    top: 92px;
    display: flex;
    align-items: center;
    justify-content: center;
    gap: 16px;
  }
  .brand-mark {
    width: 18px;
    height: 18px;
    background: var(--white);
  }
  .brand-name {
    font-family: "Archivo", sans-serif;
    font-weight: 800;
    font-size: 48px;
    line-height: 1;
    letter-spacing: 3px;
    color: var(--white);
  }
  .title { font-weight: normal; }
  .title-line {
    position: absolute;
    left: 0;
    right: 0;
    text-align: center;
    line-height: 1;
  }
  .title-article, .title-mood {
    font-family: "Archivo", sans-serif;
    font-weight: 800;
    font-size: 44px;
    letter-spacing: 1px;
  }
  .title-article { top: 234px; color: var(--berry-deep); }
  .title-mood { top: 532px; color: var(--white); }
  .title-main {
    font-family: "Playfair Display", serif;
    font-weight: 600;
    font-size: 110px;
  }
  .title-main--first {
    top: 282px;
    color: var(--white);
    text-shadow: -5px -4px 0 var(--berry-dark);
  }
  .title-main--second {
    top: 398px;
    color: var(--berry-deep);
    text-shadow: -5px -4px 0 var(--white);
  }
  .product-type {
    position: absolute;
    left: 420px;
    top: 600px;
    width: 360px;
    font-family: "Allison", cursive;
    font-size: 140px;
    line-height: 0.72;
    color: var(--berry-deep);
    transform: rotate(-6deg);
  }
  .product-type span { display: block; }
  .product-type .line-two { padding-left: 70px; }
</style>
</head>
<body>
  <main class="label">
    <div class="frost-frame" role="img" aria-label="Frosted icy branch pattern framing the label edges"></div>
    <div class="brand">
      <span class="brand-mark"></span>
      <span class="brand-name">HALMBERG</span>
    </div>
    <h1 class="title">
      <span class="title-line title-article">THE</span>
      <span class="title-line title-main title-main--first">VELVET</span>
      <span class="title-line title-main title-main--second">DUSK</span>
      <span class="title-line title-mood">MOOD</span>
    </h1>
    <p class="product-type">
      <span class="line-one">Sparkling</span>
      <span class="line-two">Wine</span>
    </p>
  </main>
</body>
</html>
```